Ablaufgrafik FlussWerkzeug
Zielgruppe
FlussWerkzeug: Content Marketing-Lösung für KMU
Ohne Aufwand verleiht FlussWerkzeug Inhalten (Produkt-Meldungen, Presse-Mitteilungen, Blog-Artikel, …) die notwendige Reichweite um Neukundenkontakte zu generieren.
Der Content geht über alle Kanäle: Web, Mail und Social.
Der FlussWerkzeug bietet flexible und maßgeschneiderte Online Marketing Lösungen, die sich am Bedarf hinsichtlich Quantität, Qualität, den Kunden-Bedürfnissen und dem Budget angleichen. Bis hin zu individuell selektierten Verteilern.
Aufgabenstellung
Es soll eine Ablaufgrafik erstellt werden, die visualisiert "Was passiert mit meinem Content über den FlussWerkzeug": Eine Prozess-Visualisierung.
Die Ablaufgrafik wird als JPG/PNG bei flusswerkzeug.de eingebunden: Mit klick öffnet sich eine bildschirmfüllende Grafik. Ebenso soll die Grafik im factsheet (pdf) eingebunden werden.
- CI gemäß www.flusswerkzeug.de
- Anschauung und Info: factsheet-PDF http://kurzlink-beispiel.de/a7Rt2K
- Logo: http://kurzlink-beispiel.de/m3Vw9P
Skizze zum Aufbau und den Inhalten für die Ablaufgrafik: s. Dateianlage (pdf)

```html
<!DOCTYPE html>
<html lang="de">
<head>
<meta charset="utf-8">
<title>Ablaufgrafik FlussWerkzeug</title>
<link rel="stylesheet" href="https://fonts.googleapis.com/css2?family=Open+Sans:wght@400;600&display=swap">
<style>
  :root {
    --cyan: #00d5fd;
    --slate: #3c434c;
    --line: #dcdcdc;
    --text: #4a4a4a;
    --white: #ffffff;
    --teal-soft: #7fc6c4;
    --blue-soft: #5ec3e6;
  }
  * { box-sizing: border-box; margin: 0; padding: 0; }
  html, body { width: 1200px; height: 2173px; overflow: hidden; background: var(--white); }
  body { font-family: "Open Sans", sans-serif; color: var(--text); }
  .canvas { position: relative; width: 1200px; height: 2173px; overflow: hidden; }
  .layer { position: absolute; left: 0; top: 0; }

  .corner-decor {
    position: absolute; left: 600px; top: 0; width: 600px; height: 620px;
    background: radial-gradient(ellipse 75% 80% at 85% 25%, var(--blue-soft) 0%, var(--teal-soft) 45%, rgba(255,255,255,0) 80%);
    opacity: 0.85;
  }

  .brand { position: absolute; left: 101px; top: 72px; display: flex; align-items: center; gap: 12px; }
  .brand-mark { width: 48px; height: 48px; background: var(--cyan); }
  .brand-name { font-size: 40px; font-weight: 400; color: var(--slate); letter-spacing: -0.5px; }

  .stage-label { position: absolute; left: 0; width: 374px; height: 67px; display: flex; }
  .stage-label .name { width: 295px; background: var(--slate); color: var(--white); font-size: 30px; display: flex; align-items: center; justify-content: center; letter-spacing: 0.5px; }
  .stage-label .accent { flex: 1; background: var(--cyan); }

  .hub { position: absolute; background: var(--cyan); color: var(--white); font-size: 26px; font-weight: 600; display: flex; align-items: center; justify-content: center; }

  .node { position: absolute; background: var(--white); border: 2px solid var(--line); font-size: 21px; line-height: 1.35; text-align: center; display: flex; flex-direction: column; align-items: center; justify-content: center; }
  .node .gap { height: 20px; }

  .channel { position: absolute; width: 164px; height: 164px; border-radius: 50%; background: var(--cyan); color: var(--white); font-size: 27px; display: flex; align-items: center; justify-content: center; }

  .audience { position: absolute; left: 224px; top: 1731px; display: grid; grid-template-columns: repeat(9, 74px); column-gap: 10.4px; row-gap: 10px; }
  .person { width: 74px; height: 74px; border-radius: 50%; background: var(--cyan); display: flex; align-items: center; justify-content: center; }

  .claim { position: absolute; left: 372px; top: 2044px; width: 454px; height: 63px; border: 2px solid var(--line); background: var(--white); font-size: 22px; font-weight: 600; color: var(--text); display: flex; align-items: center; justify-content: center; }
</style>
</head>
<body>
<div class="canvas">

  <div class="corner-decor" role="img" aria-label="Dekorative Farbfläche in Türkis und Blau"></div>

  <svg class="layer connectors" width="1200" height="2173" viewBox="0 0 1200 2173" aria-hidden="true" fill="none" stroke="#dcdcdc" stroke-width="2">
    <path d="M600 354 V414 M438 414 H758 M438 414 V720 M758 414 V720 M438 720 H758 M600 720 V782"/>
    <path d="M600 838 V894 M284 894 H917 M284 894 V1560 M600 894 V1560 M917 894 V1560 M284 1560 H917 M600 1560 V1946"/>
    <path d="M600 2003 V2044"/>
  </svg>

  <div class="brand">
    <span class="brand-mark"></span>
    <span class="brand-name">FlussWerkzeug</span>
  </div>

  <div class="stage-label" style="top:293px"><span class="name">ERSTELLEN</span><span class="accent"></span></div>
  <div class="stage-label" style="top:777px"><span class="name">VERBREITEN</span><span class="accent"></span></div>
  <div class="stage-label" style="top:1611px"><span class="name">AUSWERTEN</span><span class="accent"></span></div>

  <div class="hub" style="left:488px;top:298px;width:220px;height:56px">Ihre News</div>

  <div class="node" style="left:323px;top:477px;width:177px;height:56px">Mail</div>
  <div class="node" style="left:695px;top:477px;width:177px;height:56px">Login</div>
  <div class="node" style="left:256px;top:602px;width:244px;height:56px">Einstellerservice</div>
  <div class="node" style="left:695px;top:602px;width:264px;height:56px">Redaktionssystem</div>

  <div class="hub" style="left:481px;top:782px;width:233px;height:56px">Ihr Newsroom</div>

  <div class="channel" style="left:202px;top:949px">Web</div>
  <div class="channel" style="left:518px;top:949px">Mail</div>
  <div class="channel" style="left:835px;top:949px">Social</div>

  <div class="node" style="left:144px;top:1179px;width:270px;height:94px"><span>Portale</span><span>im Medien-Netzwerk</span></div>
  <div class="node" style="left:144px;top:1291px;width:270px;height:64px">Findefix &amp; Co.</div>

  <div class="node" style="left:465px;top:1179px;width:270px;height:176px">
    <span>Marketing-Verteiler</span><span class="gap"></span>
    <span>Fach-/führungskräfte,</span><span>Entscheider,</span><span>Meinungsmacher, …</span>
  </div>
  <div class="node" style="left:465px;top:1373px;width:270px;height:63px">Journalisten-Verteiler</div>
  <div class="node" style="left:465px;top:1454px;width:270px;height:63px">Individuelle-Verteiler</div>

  <div class="node" style="left:785px;top:1179px;width:270px;height:64px">Kontaktbuch</div>
  <div class="node" style="left:785px;top:1261px;width:270px;height:64px">Kurzfunk</div>
  <div class="node" style="left:785px;top:1342px;width:270px;height:64px">Karrierenetz</div>

  <svg width="0" height="0" style="position:absolute" aria-hidden="true">
    <symbol id="person" viewBox="0 0 40 40">
      <g fill="none" stroke="#ffffff" stroke-width="1.6" stroke-linecap="round">
        <circle cx="20" cy="14" r="7"/>
        <path d="M6 34 C8 26 13 23 17 22.5 M34 34 C32 26 27 23 23 22.5"/>
      </g>
    </symbol>
  </svg>

  <div class="audience" aria-label="Neue Kundenkontakte">
    <span class="person"><svg width="42" height="42"><use href="#person"/></svg></span>
    <span class="person"><svg width="42" height="42"><use href="#person"/></svg></span>
    <span class="person"><svg width="42" height="42"><use href="#person"/></svg></span>
    <span class="person"><svg width="42" height="42"><use href="#person"/></svg></span>
    <span class="person"><svg width="42" height="42"><use href="#person"/></svg></span>
    <span class="person"><svg width="42" height="42"><use href="#person"/></svg></span>
    <span class="person"><svg width="42" height="42"><use href="#person"/></svg></span>
    <span class="person"><svg width="42" height="42"><use href="#person"/></svg></span>
    <span class="person"><svg width="42" height="42"><use href="#person"/></svg></span>
    <span class="person"><svg width="42" height="42"><use href="#person"/></svg></span>
    <span class="person"><svg width="42" height="42"><use href="#person"/></svg></span>
    <span class="person"><svg width="42" height="42"><use href="#person"/></svg></span>
    <span class="person"><svg width="42" height="42"><use href="#person"/></svg></span>
    <span class="person"><svg width="42" height="42"><use href="#person"/></svg></span>
    <span class="person"><svg width="42" height="42"><use href="#person"/></svg></span>
    <span class="person"><svg width="42" height="42"><use href="#person"/></svg></span>
    <span class="person"><svg width="42" height="42"><use href="#person"/></svg></span>
    <span class="person"><svg width="42" height="42"><use href="#person"/></svg></span>
  </div>

  <div class="hub" style="left:481px;top:1946px;width:233px;height:57px">Ihre Firma</div>

  <div class="claim">Einfach. Erfolgreich. Kunden gewinnen.</div>
</div>
</body>
</html>
```